Text heavy poster for university audience

I have developed a set of standards for online teaching that need to be turned into a post format. The project has a logo which should be incorporated. Most of the designing will be in terms of text layout. The logo (two versions - higher quality files available) and the a sample of standards (as image - word version available; the example is one third of standards) are attached. Design that can be adapted to brochure format would be great. (Brochure adaption will be paid separately via another project to be opened here). More details available here: http://www.brivelquarto.net
Updates

Dear all,

The URL for the site needs to be include in the design - either as footer or under logo:
<http://www.brivelquarto.net>

Sorry for late notice

Target Market(s)

The are university staff

Industry/Entity Type

University

Font styles to use
Serif
Sans Serif

Requirements
Must have
• The text in the "required" attachment must be included; but for initial draft feel free to restrict your design to "sample" attachment
The green from the Logo (PANTONE 17-5641 Emerald) should be the foundation of the colour palette.
Nice to have
• The collaborators as named here: http://www.brivelquarto.net/collaborators/
My preferred find is helvetica neue, but similar can be used
Should not have
• Decorative fonts

```html
<!DOCTYPE html>
<html lang="en">
<head>
<meta charset="utf-8">
<title>Brivel Quarto – Standards poster</title>
<link rel="stylesheet" href="https://fonts.googleapis.com/css2?family=Arimo:ital,wght@0,400;0,700;1,400&display=swap">
<style>
  :root {
    --emerald: #4d9163;
    --lime: #8dc63f;
    --badge-light: #9fd35f;
    --badge-dark: #5fa53c;
    --paper: #f1f2f1;
    --rule: #c9cfc9;
    --ink: #2b2b2b;
    --ink-soft: #4a4a4a;
    --white: #ffffff;
  }
  * { box-sizing: border-box; margin: 0; padding: 0; }
  html, body { width: 1200px; height: 848px; overflow: hidden; background: var(--paper); }
  body { font-family: "Arimo", "Helvetica Neue", Arial, sans-serif; color: var(--ink); }

  .poster { position: relative; width: 1200px; height: 848px; overflow: hidden; background: var(--paper); }
  .edge { position: absolute; left: 0; width: 100%; height: 7px; background: var(--emerald); }
  .edge--top { top: 0; }
  .edge--bottom { bottom: 0; }

  /* Masthead */
  .brand { position: absolute; left: 31px; top: 40px; display: flex; align-items: center; gap: 16px; }
  .brand-mark { width: 78px; height: 78px; background: var(--emerald); }
  .brand-name { font-size: 20px; line-height: 29px; font-weight: 700; color: var(--emerald); letter-spacing: 0.5px; text-transform: uppercase; }

  .contact { position: absolute; top: 58px; left: 818px; font-size: 11px; line-height: 13px; color: var(--ink); font-style: normal; }
  .contact-lines { position: absolute; top: 58px; left: 990px; font-size: 11px; line-height: 13px; }
  .contact-lines .key { display: inline-block; width: 18px; color: var(--emerald); font-weight: 700; }
  .contact-url { position: absolute; top: 85px; left: 990px; font-size: 12.5px; font-weight: 700; color: var(--emerald); }
  .contact-rule { position: absolute; top: 96px; left: 818px; width: 345px; height: 14px; border-bottom: 1px solid var(--rule); border-right: 1px solid var(--rule); border-bottom-right-radius: 14px; }

  /* Columns */
  .column { position: absolute; top: 137px; width: 350px; }
  .column--students { left: 30px; }
  .column--staff { left: 424px; }
  .column--organisation { left: 818px; }

  .column-title { font-size: 27px; font-weight: 700; color: var(--lime); line-height: 30px; }
  .column-intro { margin-top: 4px; height: 48px; font-size: 11px; line-height: 13.5px; color: var(--ink); width: 315px; }
  .column-intro strong { font-weight: 700; }
  .column-rule { height: 11px; width: 345px; border-bottom: 1px solid var(--rule); border-right: 1px solid var(--rule); border-bottom-right-radius: 12px; margin-top: -8px; }

  .standards { list-style: none; margin-top: 0; }
  .standard { height: 74.3px; position: relative; }

  .badge {
    position: absolute; left: 0; top: 0; width: 38px; height: 38px; border-radius: 50%;
    background: radial-gradient(circle at 35% 30%, var(--badge-light), var(--badge-dark));
    border: 2px solid var(--white);
    box-shadow: 0 0 0 1px #cfd6cf;
    color: var(--white); font-size: 17px; font-weight: 700;
    display: flex; align-items: center; justify-content: center; z-index: 2;
  }
  .standard-title {
    position: absolute; left: 18px; top: 6px; width: 315px; height: 25px;
    background: var(--emerald); border-radius: 0 13px 13px 0;
    padding-left: 28px; color: var(--white);
    font-size: 8.6px; line-height: 9.8px; font-weight: 700; text-transform: uppercase; letter-spacing: 0.2px;
    display: flex; align-items: center;
  }
  .column--organisation .standard-title { width: 330px; letter-spacing: 0; }

  .levels { position: absolute; left: 48px; top: 34px; display: grid; grid-template-columns: 98px 103px 80px; }
  .level-label { font-size: 6.8px; font-weight: 700; color: var(--lime); text-transform: uppercase; line-height: 8px; }
  .level-text { font-size: 5.6px; line-height: 6.8px; color: var(--ink-soft); padding-right: 8px; }
  .level-text--pending { letter-spacing: 0.1px; }

  /* Footer */
  .licence { position: absolute; left: 424px; top: 700px; width: 345px; }
  .licence-name { font-size: 22px; font-weight: 700; color: var(--ink); line-height: 26px; }
  .licence-text { margin-top: 18px; font-size: 9px; line-height: 11px; font-style: italic; color: var(--ink); }

  .support-note { position: absolute; left: 818px; top: 745px; width: 345px; font-size: 9px; line-height: 11px; font-style: italic; color: var(--ink); }
</style>
</head>
<body>
<main class="poster">
  <div class="edge edge--top"></div>

  <header>
    <div class="brand">
      <span class="brand-mark"></span>
      <span class="brand-name">Brivel<br>Quarto</span>
    </div>
    <address class="contact">Harrowgate University<br>Eastmere NSW 2190<br>Australia</address>
    <div class="contact-lines">
      <div><span class="key">t</span>+61(0)2 9555 0187</div>
      <div><span class="key">e</span>r.allenby@hgu.edu.au</div>
    </div>
    <div class="contact-url">www.brivelquarto.net</div>
    <div class="contact-rule"></div>
  </header>

  <section class="column column--students">
    <h2 class="column-title">Students</h2>
    <p class="column-intro">Students are supported in their online learning with a quality <strong>curriculum [1-4]</strong>, opportunities for <strong>interaction</strong> with peers and staff <strong>[5&amp;6]</strong>, and appropriate <strong>support [7&amp;8]</strong>.</p>
    <div class="column-rule"></div>
    <ol class="standards">
      <li class="standard">
        <span class="badge">01</span>
        <h3 class="standard-title">Curriculum materials are aligned,<br>available and engaging.</h3>
        <dl class="levels">
          <div><dt class="level-label">Threshold:</dt><dd class="level-text">The necessary materials are constructively aligned and available online.</dd></div>
          <div><dt class="level-label">Good:</dt><dd class="level-text">The materials are provided using a variety of media to engage students and support diversity.</dd></div>
          <div><dt class="level-label">Excellent:</dt><dd class="level-text level-text--pending">XXXXXXXXXXXXXXX<br>XXXXXXXXXXXXXXX.</dd></div>
        </dl>
      </li>
      <li class="standard">
        <span class="badge">02</span>
        <h3 class="standard-title">Learning activities are aligned,<br>available and engaging.</h3>
        <dl class="levels">
          <div><dt class="level-label">Threshold:</dt><dd class="level-text">Constructively aligned learning activities are available online.</dd></div>
          <div><dt class="level-label">Good:</dt><dd class="level-text">Learning activities use a variety of appropriate technologies to engage students and support diversity.</dd></div>
          <div><dt class="level-label">Excellent:</dt><dd class="level-text level-text--pending">XXXXXXXXXXXXXXX<br>XXXXXXXXXXXXXXX.</dd></div>
        </dl>
      </li>
      <li class="standard">
        <span class="badge">03</span>
        <h3 class="standard-title">Assessment tasks are aligned,<br>available and engaging.</h3>
        <dl class="levels">
          <div><dt class="level-label">Threshold:</dt><dd class="level-text">Constructively aligned learning activities are available online.</dd></div>
          <div><dt class="level-label">Good:</dt><dd class="level-text">Learning activities use a variety of appropriate technologies to engage students and support diversity.</dd></div>
          <div><dt class="level-label">Excellent:</dt><dd class="level-text level-text--pending">XXXXXXXXXXXXXXX<br>XXXXXXXXXXXXXXX.</dd></div>
        </dl>
      </li>
      <li class="standard">
        <span class="badge">04</span>
        <h3 class="standard-title">Students are provided with timely,<br>improvement focused formative feedback.</h3>
        <dl class="levels">
          <div><dt class="level-label">Threshold:</dt><dd class="level-text">Appropriate technologies are used to provide students with formative feedback in a timely manner.</dd></div>
          <div><dt class="level-label">Good:</dt><dd class="level-text">Feedback is provided in a variety of media to engage students and support diversity.</dd></div>
          <div><dt class="level-label">Excellent:</dt><dd class="level-text level-text--pending">XXXXXXXXXXXXXXX<br>XXXXXXXXXXXXXXX.</dd></div>
        </dl>
      </li>
      <li class="standard">
        <span class="badge">05</span>
        <h3 class="standard-title">Students are provided with<br>opportunities to interact with peers.</h3>
        <dl class="levels">
          <div><dt class="level-label">Threshold:</dt><dd class="level-text">There are opportunities for social interaction.</dd></div>
          <div><dt class="level-label">Good:</dt><dd class="level-text">There are opportunities for learning-focused interaction.</dd></div>
          <div><dt class="level-label">Excellent:</dt><dd class="level-text level-text--pending">XXXXXXXXXXXXXXX<br>XXXXXXXXXXXXXXX.</dd></div>
        </dl>
      </li>
      <li class="standard">
        <span class="badge">06</span>
        <h3 class="standard-title">Students are provided with<br>opportunities to interact with staff</h3>
        <dl class="levels">
          <div><dt class="level-label">Threshold:</dt><dd class="level-text">Staff are provided with opportunities to answer student queries.</dd></div>
          <div><dt class="level-label">Good:</dt><dd class="level-text">Staff are provided with opportunities to be active participants in learning-focused interactions.</dd></div>
          <div><dt class="level-label">Excellent:</dt><dd class="level-text level-text--pending">XXXXXXXXXXXXXXX<br>XXXXXXXXXXXXXXX.</dd></div>
        </dl>
      </li>
      <li class="standard">
        <span class="badge">07</span>
        <h3 class="standard-title">Students are provided with<br>appropriate learning support.</h3>
        <dl class="levels">
          <div><dt class="level-label">Threshold:</dt><dd class="level-text">Appropriate, up-to-date and reliable learning guides and resources are provided online.</dd></div>
          <div><dt class="level-label">Good:</dt><dd class="level-text">A range of appropriate, up-to-date and reliable online learning skills workshops are available.</dd></div>
          <div><dt class="level-label">Excellent:</dt><dd class="level-text level-text--pending">XXXXXXXXXXXXXXX<br>XXXXXXXXXXXXXXX.</dd></div>
        </dl>
      </li>
      <li class="standard">
        <span class="badge">08</span>
        <h3 class="standard-title">Students are supported in their<br>use of educational technology.</h3>
        <dl class="levels">
          <div><dt class="level-label">Threshold:</dt><dd class="level-text">Appropriate, up-to-date and reliable technological guides and resources are provided online.</dd></div>
          <div><dt class="level-label">Good:</dt><dd class="level-text">Appropriate, timely and reliable asynchronous technological support is available.</dd></div>
          <div><dt class="level-label">Excellent:</dt><dd class="level-text level-text--pending">XXXXXXXXXXXXXXX<br>XXXXXXXXXXXXXXX.</dd></div>
        </dl>
      </li>
    </ol>
  </section>

  <section class="column column--staff">
    <h2 class="column-title">Staff</h2>
    <p class="column-intro">Staff are supported in their online teaching with quality <strong>professional development [9]</strong>, <strong>resourcing [10]</strong> and <strong>technical support [11]</strong>.</p>
    <div class="column-rule"></div>
    <ol class="standards">
      <li class="standard">
        <span class="badge">09</span>
        <h3 class="standard-title">Staff are provided with quality professional<br>development in online education.</h3>
        <dl class="levels">
          <div><dt class="level-label">Threshold:</dt><dd class="level-text">A range of appropriate, up-to-date and informative professional development activities are available to staff.</dd></div>
          <div><dt class="level-label">Good:</dt><dd class="level-text">The organisation requires staff to engage in continued professional development relevant to online education.</dd></div>
          <div><dt class="level-label">Excellent:</dt><dd class="level-text level-text--pending">XXXXXXXXXXXXXXX<br>XXXXXXXXXXXXXXX.</dd></div>
        </dl>
      </li>
      <li class="standard">
        <span class="badge">10</span>
        <h3 class="standard-title">Online education is recognised in workload.</h3>
        <dl class="levels">
          <div><dt class="level-label">Threshold:</dt><dd class="level-text">Online teaching is recognised in workload.</dd></div>
          <div><dt class="level-label">Good:</dt><dd class="level-text">Online unit development is recognised in workload.</dd></div>
          <div><dt class="level-label">Excellent:</dt><dd class="level-text level-text--pending">XXXXXXXXXXXXXXX<br>XXXXXXXXXXXXXXX.</dd></div>
        </dl>
      </li>
      <li class="standard">
        <span class="badge">11</span>
        <h3 class="standard-title">Staff are supported in their use<br>of educational technology.</h3>
        <dl class="levels">
          <div><dt class="level-label">Threshold:</dt><dd class="level-text">Appropriate, up-to-date and reliable technological guides and resources are provided online.</dd></div>
          <div><dt class="level-label">Good:</dt><dd class="level-text">Appropriate, timely and reliable asynchronous technological support is available.</dd></div>
          <div><dt class="level-label">Excellent:</dt><dd class="level-text level-text--pending">XXXXXXXXXXXXXXX<br>XXXXXXXXXXXXXXX.</dd></div>
        </dl>
      </li>
    </ol>
  </section>

  <section class="column column--organisation">
    <h2 class="column-title">Organisation</h2>
    <p class="column-intro">The organisation supports online education through the provision of quality <strong>leadership [12-13]</strong>, <strong>infrastructure [14]</strong> and <strong>evaluation [15-17]</strong>.</p>
    <div class="column-rule"></div>
    <ol class="standards">
      <li class="standard">
        <span class="badge">12</span>
        <h3 class="standard-title">The organisation provides strategic<br>leadership in online education.</h3>
        <dl class="levels">
          <div><dt class="level-label">Threshold:</dt><dd class="level-text">The organisation has a clearly articulated strategic position on online education.</dd></div>
          <div><dt class="level-label">Good:</dt><dd class="level-text">An appropriate member of the executive has explicit responsibility for online education.</dd></div>
          <div><dt class="level-label">Excellent:</dt><dd class="level-text level-text--pending">XXXXXXXXXXXXXXX<br>XXXXXXXXXXXXXXX.</dd></div>
        </dl>
      </li>
      <li class="standard">
        <span class="badge">13</span>
        <h3 class="standard-title">The organisation employs a systematic approach<br>to resource allocation in online education.</h3>
        <dl class="levels">
          <div><dt class="level-label">Threshold:</dt><dd class="level-text">There is a systematic approach to resource allocation.</dd></div>
          <div><dt class="level-label">Good:</dt><dd class="level-text">There is systematic approach with formal criteria that are widely available.</dd></div>
          <div><dt class="level-label">Excellent:</dt><dd class="level-text level-text--pending">XXXXXXXXXXXXXXX<br>XXXXXXXXXXXXXXX.</dd></div>
        </dl>
      </li>
      <li class="standard">
        <span class="badge">14</span>
        <h3 class="standard-title">The organisation maintains and supports a quality<br>learning platform for delivering online education.</h3>
        <dl class="levels">
          <div><dt class="level-label">Threshold:</dt><dd class="level-text">The organisation maintains and supports an appropriate learning platform.</dd></div>
          <div><dt class="level-label">Good:</dt><dd class="level-text">The learning platform provided is fit for purpose, scalable and reliable.</dd></div>
          <div><dt class="level-label">Excellent:</dt><dd class="level-text level-text--pending">XXXXXXXXXXXXXXX<br>XXXXXXXXXXXXXXX.</dd></div>
        </dl>
      </li>
      <li class="standard">
        <span class="badge">15</span>
        <h3 class="standard-title">The organisation has a process for evaluating and<br>improving student satisfaction with online education.</h3>
        <dl class="levels">
          <div><dt class="level-label">Threshold:</dt><dd class="level-text">The organisation has a systematic process for evaluating and improving student satisfaction with online education.</dd></div>
          <div><dt class="level-label">Good:</dt><dd class="level-text">The organisation has a systematic process for improving student learning outcomes and satisfaction with online education and communicating improvements to students.</dd></div>
          <div><dt class="level-label">Excellent:</dt><dd class="level-text level-text--pending">XXXXXXXXXXXXXXX<br>XXXXXXXXXXXXXXX.</dd></div>
        </dl>
      </li>
      <li class="standard">
        <span class="badge">16</span>
        <h3 class="standard-title">The organisation has a process for evaluating<br>and improving training and support for staff.</h3>
        <dl class="levels">
          <div><dt class="level-label">Threshold:</dt><dd class="level-text">The organisation has a systematic process for evaluating and improving staff training and support.</dd></div>
          <div><dt class="level-label">Good:</dt><dd class="level-text">The organisation has a systematic process for improving staff training and support and communicating improvements to staff.</dd></div>
          <div><dt class="level-label">Excellent:</dt><dd class="level-text level-text--pending">XXXXXXXXXXXXXXX<br>XXXXXXXXXXXXXXX.</dd></div>
        </dl>
      </li>
      <li class="standard">
        <span class="badge">17</span>
        <h3 class="standard-title">The organisation has a process for evaluating<br>and improving infrastructure.</h3>
        <dl class="levels">
          <div><dt class="level-label">Threshold:</dt><dd class="level-text">The organisation has a systematic process for evaluating and improving infrastructure.</dd></div>
          <div><dt class="level-label">Good:</dt><dd class="level-text">The organisation has a systematic process for improving infrastructure and communicating improvements to stakeholders.</dd></div>
          <div><dt class="level-label">Excellent:</dt><dd class="level-text level-text--pending">XXXXXXXXXXXXXXX<br>XXXXXXXXXXXXXXX.</dd></div>
        </dl>
      </li>
    </ol>
  </section>

  <footer>
    <div class="licence">
      <div class="licence-name">Openshare Licensing Trust</div>
      <p class="licence-text">This work is shared under the Openshare Licensing Trust Open Reuse Licence, Second Edition. To read the full terms of this licence, visit http://openshare-trust.org/reuse-terms or send a letter to the Openshare Licensing Trust, 218 Larkin Way, Suite 400, Fairhaven, Oregon, 97001, USA.</p>
    </div>
    <p class="support-note">Support for this activity has been provided by the National Office for Tertiary Teaching. The views expressed in this activity do not necessarily reflect the views of the National Office for Tertiary Teaching.</p>
  </footer>

  <div class="edge edge--bottom"></div>
</main>
</body>
</html>
```